Album Cover Design – TAVREN “Sable Hours”

Hello, we are Corvane Records, representing artist TAVREN, who will release his second album on October 24, 2025. We are looking for a high-quality, artistic album cover design that will represent this new era of his music.
About the album:
Sable Hours represents a darker, bolder alter ego of TAVREN. It’s powerful, emotional, and mysterious - a step into a new world. The visuals should reflect this alter ego and dark chic mood of this era.
The first single, “KORAL,” is already released and sets the tone: vibrant but with an edge, bold and energetic.

Style we are looking for:
• Dark, bold, mysterious, yet elegant and premium
• Visually striking and memorable
• Modern and international feel

Additional guidance for designers:
Please research TAVREN to understand his style and artistic direction:
• YouTube: https://www.vidstreamhub.example/channel/QX7pLmR3vTnWcHsYdKeAbGfZ
• Website: www.tavren-music.example
Think of an iconic, timeless cover that captures both the darkness and the charisma of TAVREN.

Deliverables:
• Final album cover design (digital + print)
• Source files

```html
<!DOCTYPE html>
<html lang="en">
<head>
<meta charset="utf-8">
<title>TAVREN – Sable Hours</title>
<link rel="stylesheet" href="https://fonts.googleapis.com/css2?family=Oranienbaum&family=Dosis:wght@600&display=swap">
<style>
  :root {
    --stage: #5f5f5f;
    --cover-black: #0b0b0b;
    --cover-edge: #1c1c1c;
    --ink-white: #f4f4f2;
    --echo-1: #3a3a3a;
    --echo-2: #2a2a2a;
    --echo-3: #1c1c1c;
    --photo-light: #8a8a8a;
    --photo-mid: #3b3b3b;
  }
  * { margin: 0; padding: 0; box-sizing: border-box; }
  html, body {
    width: 1200px;
    height: 637px;
    overflow: hidden;
    background: var(--stage);
  }
  .stage {
    width: 1200px;
    height: 637px;
    display: flex;
    align-items: center;
    justify-content: center;
  }
  .album-cover {
    position: relative;
    width: 597px;
    height: 597px;
    overflow: hidden;
    background:
      radial-gradient(ellipse at 50% 50%, var(--cover-black) 70%, var(--cover-edge) 100%);
  }
  .artist-title,
  .title-echo {
    position: absolute;
    left: 0;
    width: 100%;
    text-align: center;
    font-family: "Oranienbaum", "Times New Roman", serif;
    font-size: 118px;
    line-height: 1;
    letter-spacing: 1px;
    transform: scaleX(0.82) scaleY(1.05);
    transform-origin: center top;
  }
  .title-echo { z-index: 1; }
  .title-echo--one   { top: 160px; color: var(--echo-1); }
  .title-echo--two   { top: 242px; color: var(--echo-2); }
  .title-echo--three { top: 324px; color: var(--echo-3); }
  .portrait {
    position: absolute;
    z-index: 2;
    left: 150px;
    top: 120px;
    width: 420px;
    height: 477px;
    background:
      radial-gradient(ellipse 42% 30% at 38% 38%, var(--photo-light) 0%, var(--photo-mid) 55%, transparent 100%),
      radial-gradient(ellipse 60% 45% at 55% 80%, var(--photo-mid) 0%, transparent 100%);
    opacity: 0.85;
  }
  .artist-title {
    z-index: 3;
    top: 36px;
    color: var(--ink-white);
  }
  .album-name {
    position: absolute;
    z-index: 3;
    right: 58px;
    bottom: 26px;
    font-family: "Dosis", "Arial Narrow", sans-serif;
    font-weight: 600;
    font-size: 34px;
    letter-spacing: 1px;
    color: var(--ink-white);
  }
</style>
</head>
<body>
  <main class="stage">
    <section class="album-cover">
      <div class="title-echo title-echo--one" aria-hidden="true">TAVREN</div>
      <div class="title-echo title-echo--two" aria-hidden="true">TAVREN</div>
      <div class="title-echo title-echo--three" aria-hidden="true">TAVREN</div>
      <div class="portrait" role="img" aria-label="Black and white portrait of the artist, shirtless with tattoos, chin resting on his fist, emerging from shadow"></div>
      <h1 class="artist-title">TAVREN</h1>
      <p class="album-name">SABLE HOURS</p>
    </section>
  </main>
</body>
</html>
```